Stationery Design Project

KV7 Staffing requires letterhead and business card designs for a company based in London. Just like the name, we're a management resourcing company, providing resources to third party companies. You can see www.kv7staffing.example for ideas on existing colour schemes and design concepts that have been implimented and agreed to. Ultimately the design should broadcast professionalism, safety and the concept of growth.

Target Market(s)

Financial institutes; friendly societies (All UK based)

Industry/Entity Type

Safety

Requirements
Must have
• Files produced should be print ready; and the text in them editable (eg address, name etc)

```html
<!DOCTYPE html>
<html lang="en">
<head>
<meta charset="utf-8">
<title>KV7 Staffing — Stationery</title>
<link rel="stylesheet" href="https://fonts.googleapis.com/css2?family=Open+Sans:wght@400;600;700&display=swap">
<style>
  :root {
    --teal-dark: #1a8a8a;
    --teal-mid: #5fc4c6;
    --teal-pale: #e4f4f8;
    --sky: #d6eefa;
    --ink: #333b3f;
    --paper: #ffffff;
    --backdrop: #ecebe8;
  }
  * { margin: 0; padding: 0; box-sizing: border-box; }
  html, body { width: 1200px; height: 900px; overflow: hidden; }
  body {
    background: var(--backdrop);
    font-family: "Open Sans", Arial, sans-serif;
    position: relative;
  }

  /* Letterhead */
  .letterhead {
    position: absolute; left: 126px; top: 20px;
    width: 606px; height: 858px;
    background: var(--paper);
    overflow: hidden;
  }
  .letterhead .brand {
    position: absolute; left: 42px; top: 36px;
    font-size: 30px; font-weight: 700; color: var(--teal-dark);
    letter-spacing: -0.5px;
  }
  .letterhead .address {
    position: absolute; left: 357px; top: 42px;
    padding-left: 10px; border-left: 1.5px solid var(--teal-mid);
    font-size: 11.5px; line-height: 16px; color: var(--ink);
    height: 50px; padding-top: 4px;
  }
  .letterhead .footer-wave {
    position: absolute; left: 0; bottom: 0; width: 606px; height: 122px;
  }
  .letterhead .web {
    position: absolute; right: 30px; bottom: 14px;
    font-size: 11.5px; color: #fff; letter-spacing: 2.4px;
  }

  /* Business cards */
  .card {
    position: absolute; left: 774px; width: 256px; height: 147px;
    border-radius: 9px; overflow: hidden;
  }
  .card-front {
    top: 229px;
    background: linear-gradient(90deg, #ffffff 0%, #f1f9fd 45%, var(--sky) 100%);
  }
  .card-back {
    top: 392px;
    background: linear-gradient(90deg, #ffffff 0%, var(--sky) 100%);
  }
  .card svg.wave { position: absolute; left: 0; top: 0; width: 256px; height: 147px; }

  .card-front .person { position: absolute; left: 14px; top: 24px; }
  .card-front .person-name { font-size: 8.5px; font-weight: 700; color: var(--teal-dark); }
  .card-front .person-role { font-size: 6.5px; color: var(--teal-dark); margin-top: 1px; }
  .card-front .contacts {
    position: absolute; left: 14px; top: 54px; list-style: none;
    font-size: 5.6px; line-height: 8.8px; color: var(--ink);
  }
  .card-front .contacts li { display: flex; align-items: center; gap: 8px; }
  .card-front .contacts svg { width: 6px; height: 6px; fill: var(--ink); }
  .card-front .brand {
    position: absolute; left: 120px; top: 44px;
    font-size: 16px; font-weight: 700; color: var(--teal-dark);
  }

  .card-back .brand {
    position: absolute; left: 0; right: 0; top: 76px; text-align: center;
    font-size: 20px; font-weight: 700; color: #fff;
  }
  .card-back .web {
    position: absolute; left: 0; right: 0; top: 129px; text-align: center;
    font-size: 6.5px; color: #fff; letter-spacing: 1.4px;
  }
</style>
</head>
<body>

<section class="letterhead" aria-label="Letterhead">
  <div class="brand">KV7 Staffing</div>
  <address class="address" style="font-style:normal">
    48 Harrow Lane 9 Kestrel Court<br>Camden, UK N1 4RT
  </address>
  <svg class="footer-wave" viewBox="0 0 606 122" preserveAspectRatio="none" aria-hidden="true">
    <path d="M0,14 C160,50 360,-8 606,10 L606,122 L0,122 Z" fill="var(--teal-pale)"/>
    <path d="M0,14 C160,50 360,-8 606,10" fill="none" stroke="var(--teal-mid)" stroke-width="3"/>
    <path d="M0,56 C190,98 380,8 606,18 L606,122 L0,122 Z" fill="var(--teal-mid)"/>
    <path d="M0,78 C210,102 400,26 606,24 L606,122 L0,122 Z" fill="var(--teal-dark)"/>
  </svg>
  <div class="web">www.kv7staffing.example</div>
</section>

<section class="card card-front" aria-label="Business card front">
  <svg class="wave" viewBox="0 0 256 147" aria-hidden="true">
    <path d="M0,112 C70,128 150,95 256,104 L256,147 L0,147 Z" fill="var(--teal-pale)"/>
    <path d="M0,112 C70,128 150,95 256,104" fill="none" stroke="var(--teal-mid)" stroke-width="1.6"/>
    <path d="M0,124 C80,140 160,98 256,110 L256,147 L0,147 Z" fill="var(--teal-mid)"/>
    <path d="M0,136 C90,146 170,108 256,120 L256,147 L0,147 Z" fill="var(--teal-dark)"/>
  </svg>
  <div class="person">
    <div class="person-name">Oliver Brandt</div>
    <div class="person-role">Director</div>
  </div>
  <ul class="contacts">
    <li><svg viewBox="0 0 10 10"><rect x="3" y="0" width="4" height="10" rx="1"/></svg>020-500-7781</li>
    <li><svg viewBox="0 0 10 10"><path d="M1,3 Q5,0 9,3 L8,5 L6,4 L4,4 L2,5 Z M2,6 H8 V9 H2 Z"/></svg>020-502-4410</li>
    <li><svg viewBox="0 0 10 10"><rect x="1" y="3" width="8" height="6"/><rect x="3" y="0" width="4" height="3"/></svg>020-502-4410</li>
    <li><svg viewBox="0 0 10 10"><path d="M0.5,2 H9.5 V8 H0.5 Z" fill="none" stroke="var(--ink)" stroke-width="1"/><path d="M0.5,2 L5,6 L9.5,2" fill="none" stroke="var(--ink)" stroke-width="1"/></svg>oliver@kv7staffing.example</li>
    <li><svg viewBox="0 0 10 10"><circle cx="5" cy="5" r="4.2" fill="none" stroke="var(--ink)" stroke-width="1"/><path d="M1,5 H9 M5,1 V9" stroke="var(--ink)" stroke-width="0.8"/></svg>kv7staffing.example</li>
  </ul>
  <div class="brand">KV7 Staffing</div>
</section>

<section class="card card-back" aria-label="Business card back">
  <svg class="wave" viewBox="0 0 256 147" aria-hidden="true">
    <defs>
      <linearGradient id="backTeal" x1="0" y1="0" x2="1" y2="1">
        <stop offset="0" stop-color="#1d9393"/>
        <stop offset="1" stop-color="#136f72"/>
      </linearGradient>
    </defs>
    <path d="M0,40 C70,26 160,18 230,22 L256,26" fill="none" stroke="var(--teal-mid)" stroke-width="1.4"/>
    <path d="M0,52 C80,36 170,24 256,40 L256,147 L0,147 Z" fill="var(--teal-mid)"/>
    <path d="M0,62 C90,44 180,30 256,52 L256,147 L0,147 Z" fill="url(#backTeal)"/>
  </svg>
  <div class="brand">KV7 Staffing</div>
  <div class="web">www.kv7staffing.example</div>
</section>

</body>
</html>
```